Lanternfield Voyages Business Card Design for Home Based Travel Agency

We already have a logo and I would like to see about getting a Business Card Design. The font on the logo can be changed. We are a home based travel agency and sell cruises and tour packages, etc. I would like the following information put into the design Name of Company and Tag Line from the logo. I would also like the email info@lanternfieldvoyages.example Phone 555-238-6140. Website www.lanternfieldvoyages.example. My name Neil Parton Travel Consultant and my wife's Name Mavis Parton. I would like you to use your imagination as nothing is off limites. Impress Me!

Target Market(s)

Baby Boomers

Industry/Entity Type

Travel Agent

Contact Information for Business Card

See above

Font styles to use
Serif
Sans Serif

Colors

Designer to choose colors to be used in the design.

Requirements
Must have
• Play with different fonts and needs to be easily readable, i.e. not too small of print.
Nice to have
• Use your imagination

```html
<!DOCTYPE html>
<html lang="en">
<head>
<meta charset="utf-8">
<title>Lanternfield Voyages – Business Card</title>
<link href="https://fonts.googleapis.com/css2?family=Cormorant+Garamond:wght@500&family=Great+Vibes&family=Open+Sans:wght@300;400;700&display=swap" rel="stylesheet">
<style>
  :root {
    --plum: #45334a;
    --paper: #ffffff;
    --ink: #111111;
    --grey: #7a7a7a;
    --soft-grey: #8a8a8a;
    --backdrop: #3b3b39;
    --accent: #f08a24;
  }
  * { margin: 0; padding: 0; box-sizing: border-box; }
  html, body { width: 960px; height: 1200px; overflow: hidden; }
  body { background: var(--backdrop); position: relative; font-family: "Open Sans", sans-serif; }

  .card { position: absolute; left: 78px; width: 817px; height: 467px; }
  .card-front { top: 77px; background: var(--plum); }
  .card-back { top: 609px; display: flex; }

  .brand { position: absolute; left: 0; right: 0; text-align: center; color: var(--paper); }
  .brand-name {
    display: inline-flex; align-items: center; gap: 14px;
    font-family: "Cormorant Garamond", serif; font-weight: 500; color: var(--paper);
    white-space: nowrap; line-height: 1.2;
  }
  .brand-mark { background: var(--accent); display: inline-block; }
  .tagline { font-family: "Open Sans", sans-serif; font-weight: 300; color: var(--paper); line-height: 1.3; }

  .card-front .brand { top: 262px; }
  .card-front .brand-name { font-size: 50px; }
  .card-front .brand-mark { width: 22px; height: 22px; }
  .card-front .tagline { font-size: 17px; margin-top: 12px; }

  .back-brand-panel { position: relative; width: 416px; height: 100%; background: var(--plum); }
  .back-brand-panel .brand { top: 228px; }
  .back-brand-panel .brand-name { font-size: 31px; gap: 9px; }
  .back-brand-panel .brand-mark { width: 14px; height: 14px; }
  .back-brand-panel .tagline { font-size: 11px; margin-top: 10px; }

  .contact-panel { position: relative; flex: 1; background: var(--paper); text-align: center; }
  .consultant-names {
    position: absolute; top: 140px; left: 0; right: 0;
    font-family: "Great Vibes", cursive; font-size: 31px; line-height: 1.3; color: var(--ink); white-space: nowrap;
  }
  .consultant-role {
    position: absolute; top: 190px; left: 0; right: 0;
    font-size: 15px; font-weight: 700; letter-spacing: 7.4px; color: var(--grey); padding-left: 8px;
  }
  .divider { position: absolute; top: 236px; left: 107px; width: 212px; height: 2px; background: var(--ink); }
  .phone { position: absolute; top: 256px; left: 0; right: 0; font-size: 26px; font-weight: 700; color: var(--ink); }
  .contact-list { position: absolute; top: 300px; left: 80px; list-style: none; }
  .contact-list li {
    display: flex; align-items: center; gap: 10px;
    font-size: 15.5px; color: var(--soft-grey); height: 24px;
  }
  .contact-list svg { width: 13px; height: 13px; flex: none; }
</style>
</head>
<body>
  <section class="card card-front">
    <div class="brand">
      <div class="brand-name"><span class="brand-mark"></span>Lanternfield Voyages</div>
      <p class="tagline">Every Journey is a Tale Worth Telling</p>
    </div>
  </section>

  <section class="card card-back">
    <div class="back-brand-panel">
      <div class="brand">
        <div class="brand-name"><span class="brand-mark"></span>Lanternfield Voyages</div>
        <p class="tagline">Every Journey is a Tale Worth Telling</p>
      </div>
    </div>
    <div class="contact-panel">
      <p class="consultant-names">Neil Parton &amp; Mavis Parton</p>
      <p class="consultant-role">TRAVEL CONSULTANT</p>
      <div class="divider"></div>
      <p class="phone">555-238-6140</p>
      <ul class="contact-list">
        <li>
          <svg viewBox="0 0 14 14" aria-hidden="true"><rect x="1" y="3" width="12" height="8" fill="#222"/><path d="M1 3 L7 8 L13 3" stroke="#fff" stroke-width="1.2" fill="none"/></svg>
          info@lanternfieldvoyages.example
        </li>
        <li>
          <svg viewBox="0 0 14 14" aria-hidden="true"><circle cx="7" cy="7" r="6" fill="#222"/><path d="M7 1 C4 4 4 10 7 13 M7 1 C10 4 10 10 7 13 M1 7 H13" stroke="#fff" stroke-width="0.9" fill="none"/></svg>
          www.lanternfieldvoyages.example
        </li>
      </ul>
    </div>
  </section>
</body>
</html>
```